Marisol transparent business card

I would like to have a transparent business card created.
A simple yet classy card with
Website www.MarisolPennington.example
Phone # 555-214-7396
I would like my full photo on the card as well as my logo.

Target Market(s)

The business card will be printed on transparent card stock.
Www.MarisolPennington.example
Phone 555-214-7396
I would like my pic on the card and my logo
Author, Speaker, & Wealth architect

Industry/Entity Type

Business

Contact Information for Business Card

Www.MarisolPennington.example
Phone 555-214-7396

Font styles to use
Serif
Decorative
Script

Requirements
Must have
• The business card will be printed on transparent card stock.
• Www.MarisolPennington.example
• Phone 555-214-7396
• I would like my pic on the card and my logo
• Author, Speaker, & Wealth architect
Nice to have
• If I could have the tattoo on my pic blurred out or airbrushed over

```html
<!DOCTYPE html>
<html lang="en">
<head>
<meta charset="utf-8">
<title>Marisol Pennington – Business Card</title>
<link href="https://fonts.googleapis.com/css2?family=Great+Vibes&family=Cormorant+Garamond:wght@500;600&display=swap" rel="stylesheet">
<style>
  :root {
    --page-bg: #f4f4f3;
    --card-bg: #fbfbfa;
    --card-edge: #e2e2e0;
    --gold: #d4a62a;
    --gold-light: #e9c862;
    --gold-deep: #c4922a;
    --ink: #3a3430;
    --ink-soft: #5a524b;
    --photo-dark: #2a2322;
    --photo-mid: #6b4a3a;
  }
  html, body {
    margin: 0;
    width: 1200px;
    height: 1200px;
    overflow: hidden;
    background: var(--page-bg);
  }
  .card {
    position: absolute;
    left: 60px;
    top: 294px;
    width: 1080px;
    height: 612px;
    background: var(--card-bg);
    border: 1px solid var(--card-edge);
    box-shadow: 0 10px 30px rgba(0,0,0,0.08);
    overflow: hidden;
    font-family: "Cormorant Garamond", Georgia, serif;
  }
  .card p, .card h1 { margin: 0; line-height: 1; white-space: nowrap; }
  .portrait {
    position: absolute;
    left: 84px;
    top: 12px;
    width: 216px;
    height: 521px;
    border-radius: 90px 90px 6px 6px;
    background: linear-gradient(180deg, var(--photo-mid) 0%, var(--photo-dark) 28%, var(--photo-dark) 100%);
  }
  .brand-mark {
    position: absolute;
    left: 560px;
    top: 96px;
    height: 82px;
    display: flex;
    align-items: center;
    gap: 14px;
  }
  .brand-mark svg { display: block; }
  .brand-mark span {
    font-size: 20px;
    font-weight: 600;
    letter-spacing: 2px;
    color: var(--gold);
    text-transform: uppercase;
  }
  .name {
    position: absolute;
    left: 384px;
    top: 212px;
    width: 576px;
    text-align: center;
    font-family: "Great Vibes", cursive;
    font-size: 60px;
    font-weight: 400;
    color: var(--ink);
  }
  .name .first { color: var(--gold); }
  .tagline {
    position: absolute;
    left: 521px;
    top: 294px;
    width: 432px;
    text-align: center;
    font-size: 16px;
    font-weight: 600;
    letter-spacing: 0.3px;
    color: var(--ink);
    text-transform: uppercase;
  }
  .roles {
    position: absolute;
    left: 372px;
    top: 366px;
    width: 610px;
    text-align: center;
    font-size: 32px;
    font-weight: 500;
    font-variant: small-caps;
    color: var(--ink-soft);
  }
  .phone {
    position: absolute;
    right: 113px;
    top: 472px;
    font-size: 30px;
    font-weight: 500;
    color: var(--ink-soft);
  }
  .web-band {
    position: absolute;
    left: 0;
    bottom: 0;
    width: 100%;
    height: 79px;
    background: linear-gradient(90deg, var(--gold-light) 0%, var(--gold) 45%, var(--gold-deep) 100%);
  }
  .web-band span {
    position: absolute;
    left: 490px;
    width: 487px;
    top: 24px;
    text-align: center;
    font-size: 31px;
    line-height: 1;
    font-weight: 500;
    color: #ffffff;
    white-space: nowrap;
  }
</style>
</head>
<body>
  <div class="card">
    <div class="portrait" role="img" aria-label="Full-length portrait of Marisol Pennington in a black dress, arms crossed"></div>

    <div class="brand-mark">
      <svg width="82" height="82" viewBox="0 0 82 82" aria-hidden="true">
        <circle cx="41" cy="41" r="37" fill="none" stroke="var(--gold)" stroke-width="4"/>
      </svg>
      <span>Marisol Pennington</span>
    </div>

    <h1 class="name"><span class="first">Marisol</span> Pennington</h1>
    <p class="tagline">Live your life on purpose, no excuses</p>
    <p class="roles">Author, Speaker, &amp; Wealth architect</p>
    <p class="phone">555-214-7396</p>

    <div class="web-band"><span>www.MarisolPennington.example</span></div>
  </div>
</body>
</html>
```